Corporate Wall Mural for Office

We have several offices across North America and we want to have a corporate wall mural in each office, so we require a mural wall design that can be adjusted for different wall dimensions and still look good.

The first mural will be 239.5" x 112.5" it will be in our Toronto office - so the background city will be the Toronto skyline

I have attached a draft design and the content PNG file.

We want a different design that keeps the content outlined in the Mural Design Content PNG file.

Our corporate font is Gilroy Semi Bold

Our corporate colors are
Blue
C94
M70
Y0
K12
Pantone 2945C

Purple
C 80
M 78
PMS 2368 C

Sky Blue
C68
M34
PMS 2727 C
Our website is qalverpoint.com

Founded in 2012, QPT is a leading provider of technology infrastructure solutions, specializing in Broadband, DAS/Private Networks, Fixed Wireless Access, Site Solutions, Carrier Networks, and Test & Measurement. Our mission is to empower organizations of all sizes with innovative connectivity and telecom infrastructure solutions to build the future of communications.

Target Market(s)

Target is the staff and visitors of our office

Industry/Entity Type

network infrastructure: both wireless and wireline

Font styles to use
Sans Serif
Other font styles liked:
• Gilroy Semi-Bold and Bold

Colors
0054AA
0677BA
7BADD7
CADEEF
E8F1F8

Requirements
Must have
• the info listed in the Mural Content.png file, our corporate colors. It should be bright and energetic.
Nice to have
• I like concept of the city silhouette from the draft design

```html
<!DOCTYPE html>
<html lang="en">
<head>
<meta charset="utf-8">
<title>QPT Office Wall Mural</title>
<link rel="stylesheet" href="https://fonts.googleapis.com/css2?family=Poppins:wght@500;600;700;800&display=swap">
<style>
  :root {
    --blue-deep: #0054aa;
    --blue-mid: #0677ba;
    --blue-brand: #1f5fc4;
    --blue-sky: #7badd7;
    --blue-pale: #cadeef;
    --blue-mist: #e8f1f8;
    --navy: #141c3a;
    --graphite: #3a3e48;
    --white: #ffffff;
    --page: #eef0f3;
  }
  * { margin: 0; padding: 0; box-sizing: border-box; }
  html, body {
    width: 1059px; height: 1200px; overflow: hidden;
    background: var(--page);
    font-family: "Poppins", sans-serif;
  }
  .mural {
    position: absolute; left: 0; top: 352px;
    width: 1059px; height: 495px; overflow: hidden;
  }
  .mural-art { position: absolute; inset: 0; }
  .t { position: absolute; line-height: 1.2; }

  .brand {
    left: 112px; top: 30px; display: flex; align-items: center; gap: 12px;
  }
  .brand-dot { width: 46px; height: 46px; border-radius: 50%; background: var(--blue-brand); }
  .brand-name { font-size: 50px; font-weight: 700; color: var(--navy); letter-spacing: 1px; line-height: 1; }

  .unique-title { left: 112px; top: 110px; font-size: 15px; font-weight: 700; color: var(--blue-brand); }
  .tag {
    position: absolute; left: 112px; height: 12px; padding: 0 6px;
    background: var(--blue-brand); color: var(--white);
    font-size: 7.5px; font-weight: 600; line-height: 12px;
  }
  .tag-line { left: 112px; font-size: 7.5px; font-weight: 500; color: var(--navy); white-space: nowrap; }

  .values-pill {
    left: 165px; top: 222px; width: 172px; height: 24px;
    border: 1.5px solid var(--blue-brand); border-radius: 4px; background: var(--white);
    color: var(--blue-brand); font-size: 12px; font-weight: 700;
    text-align: center; line-height: 21px;
  }
  .value-label {
    width: 44px; text-align: center; color: var(--white);
    font-size: 5px; font-weight: 600; line-height: 1.25; top: 324px;
  }

  .headline {
    left: 414px; top: 90px; font-size: 24px; font-weight: 800;
    color: var(--blue-brand); line-height: 1.12;
  }
  .subline { left: 414px; top: 152px; font-size: 12px; font-weight: 700; color: var(--navy); line-height: 1.25; }

  .pill-title { font-size: 13px; font-weight: 700; text-align: center; }
  .pill-light { color: var(--blue-brand); }
  .pill-dark { color: var(--white); }

  .list { list-style: none; font-size: 8px; font-weight: 600; line-height: 10.5px; white-space: nowrap; }
  .list li::before { content: "- "; }
  .list-light { color: var(--white); }
  .list-dark { color: var(--blue-deep); font-size: 8.5px; line-height: 12.5px; }
</style>
</head>
<body>
<main class="mural">
  <svg class="mural-art" viewBox="0 0 1059 495" width="1059" height="495" xmlns="http://www.w3.org/2000/svg">
    <defs>
      <linearGradient id="bg" x1="0" y1="0" x2="1" y2="1">
        <stop offset="0" stop-color="#f2f4fc"/>
        <stop offset="1" stop-color="#d8e0f3"/>
      </linearGradient>
      <linearGradient id="city" x1="0" y1="0" x2="0" y2="1">
        <stop offset="0" stop-color="#dfe5f6" stop-opacity="0"/>
        <stop offset="0.35" stop-color="#b7c6e8"/>
        <stop offset="0.75" stop-color="#6f88c2"/>
        <stop offset="1" stop-color="#34508e"/>
      </linearGradient>
      <linearGradient id="band" x1="0" y1="0" x2="1" y2="1">
        <stop offset="0" stop-color="#3d7fe0"/>
        <stop offset="1" stop-color="#1a4fb0"/>
      </linearGradient>
      <linearGradient id="tri" x1="0" y1="0" x2="0" y2="1">
        <stop offset="0" stop-color="#4f88de" stop-opacity="0.95"/>
        <stop offset="1" stop-color="#1d4fae" stop-opacity="0.95"/>
      </linearGradient>
      <linearGradient id="column" x1="0" y1="0" x2="0" y2="1">
        <stop offset="0" stop-color="#3a7ad8"/>
        <stop offset="1" stop-color="#0f3f98"/>
      </linearGradient>
      <linearGradient id="pillBlue" x1="0" y1="0" x2="1" y2="0">
        <stop offset="0" stop-color="#2f6fd2"/>
        <stop offset="1" stop-color="#1a4fb0"/>
      </linearGradient>
    </defs>

    <rect class="backdrop" width="1059" height="495" fill="url(#bg)"/>
    <polygon class="backdrop-facet" points="393,0 630,0 850,165 393,330" fill="#ffffff" opacity="0.35"/>

    <rect class="skyline" x="345" y="190" width="714" height="305" fill="url(#city)" role="img" aria-label="Night city skyline with lit high-rise towers"/>

    <rect class="side-panel" x="0" y="0" width="392" height="495" fill="#ffffff" opacity="0.55"/>
    <line class="divider" x1="393" y1="18" x2="393" y2="480" stroke="#9fb3d9" stroke-width="1.2"/>

    <polygon class="corner-top-left" points="0,0 150,0 0,55" fill="url(#band)" opacity="0.8"/>

    <polygon class="chevron-band" points="630,0 700,0 850,100 1000,0 1059,0 1059,30 850,165" fill="url(#band)"/>
    <polygon class="stripe-dark" points="900,0 960,0 1059,68 1059,112" fill="var(--graphite)"/>
    <polygon class="stripe-blue" points="985,0 1059,0 1059,48" fill="url(#band)"/>

    <polygon class="corner-band" points="0,340 0,495 345,495" fill="url(#band)"/>
    <polygon class="corner-stripe-dark" points="150,352 186,352 290,495 252,495" fill="var(--graphite)"/>
    <polygon class="corner-stripe-dark" points="205,402 228,402 295,495 272,495" fill="#22262f"/>
    <polygon class="corner-band-right" points="300,495 392,410 392,495" fill="url(#band)"/>
    <rect class="base-strip" x="990" y="478" width="69" height="17" fill="url(#band)"/>

    <rect class="headline-panel" x="405" y="84" width="340" height="60" fill="#ffffff" opacity="0.85"/>

    <path class="values-connector" d="M251 246 V262 M132 262 H333 M132 262 V276 M180 262 V276 M230 262 V276 M280 262 V276 M333 262 V276" stroke="var(--blue-brand)" stroke-width="1.4" fill="none"/>
    <g class="value-columns" fill="url(#column)">
      <rect x="114" y="295" width="36" height="117" rx="4"/>
      <rect x="162" y="295" width="36" height="117" rx="4"/>
      <rect x="212" y="295" width="36" height="117" rx="4"/>
      <rect x="262" y="295" width="36" height="117" rx="4"/>
      <rect x="315" y="295" width="36" height="117" rx="4"/>
    </g>
    <g class="value-badges" fill="#ffffff" stroke="var(--blue-brand)" stroke-width="2">
      <circle cx="132" cy="295" r="18"/>
      <circle cx="180" cy="295" r="18"/>
      <circle cx="230" cy="295" r="18"/>
      <circle cx="280" cy="295" r="18"/>
      <circle cx="333" cy="295" r="18"/>
    </g>
    <g class="value-icons" fill="var(--blue-brand)">
      <circle cx="132" cy="290" r="4"/>
      <path d="M124 303 a8 7 0 0 1 16 0 z"/>
      <rect x="172" y="296" width="3" height="6"/>
      <rect x="177" y="292" width="3" height="10"/>
      <rect x="182" y="288" width="3" height="14"/>
      <rect x="187" y="285" width="3" height="17"/>
      <circle cx="230" cy="288" r="3.5"/>
      <circle cx="222" cy="292" r="2.5"/>
      <circle cx="238" cy="292" r="2.5"/>
      <path d="M223 303 a7 7 0 0 1 14 0 z"/>
      <path d="M273 286 h14 v4 a7 7 0 0 1 -14 0 z"/>
      <rect x="278" y="296" width="4" height="4"/>
      <rect x="275" y="300" width="10" height="3"/>
      <circle cx="333" cy="291" r="6"/>
      <rect x="330" y="297" width="6" height="5"/>
    </g>

    <polygon class="capabilities-shape" points="405,228 698,228 551,363" fill="url(#tri)" stroke="#ffffff" stroke-width="1.5"/>
    <polygon class="markets-shape" points="750,228 1040,228 895,363" fill="url(#tri)" stroke="#ffffff" stroke-width="1.5"/>
    <polygon class="solutions-shape" points="735,232 562,405 908,405" fill="#f4f7fd" opacity="0.88" stroke="#9ebbe6" stroke-width="1.5"/>

    <rect class="capabilities-pill" x="452" y="222" width="198" height="26" rx="13" fill="#ffffff"/>
    <rect class="markets-pill" x="790" y="216" width="136" height="26" rx="13" fill="#ffffff"/>
    <rect class="solutions-pill" x="625" y="284" width="220" height="28" rx="14" fill="url(#pillBlue)" stroke="#ffffff" stroke-width="1.5"/>
  </svg>

  <div class="t brand"><span class="brand-dot"></span><span class="brand-name">QPT</span></div>

  <h2 class="t unique-title">WHAT MAKES US UNIQUE?</h2>
  <span class="tag" style="top:135px">QPT Touch</span>
  <p class="t tag-line" style="top:149px">We are more than a catalog</p>
  <span class="tag" style="top:164px">QPT Experience</span>
  <p class="t tag-line" style="top:178px">A pleasure to do business with: Proactive, Professional and Precise</p>
  <span class="tag" style="top:193px">QPT Solution</span>
  <p class="t tag-line" style="top:207px">Design, Develop, and Deliver Custom Solutions; On-Time and On-Spec</p>

  <div class="t values-pill">OUR CORE VALUES</div>
  <span class="t value-label" style="left:110px">People<br>First</span>
  <span class="t value-label" style="left:158px">Continuous<br>Improvement</span>
  <span class="t value-label" style="left:208px">Customer<br>Focus</span>
  <span class="t value-label" style="left:258px">Results<br>Matter</span>
  <span class="t value-label" style="left:311px">Intellectual<br>Curiosity</span>

  <h1 class="t headline">ENABLING SOLUTIONS<br>FOR A CONNECTED WORLD</h1>
  <p class="t subline">We Distribute Products and Solution Services<br>for Digital Infrastructure</p>

  <h3 class="t pill-title pill-light" style="left:452px; top:227px; width:198px">OUR CAPABILITIES</h3>
  <ul class="t list list-light" style="left:498px; top:251px">
    <li>Wireless Infrastructure</li>
    <li>Broadband &amp; Fiber Site Solutions</li>
    <li>Fixed Wireless Acess</li>
    <li>Test &amp; Measurement</li>
    <li>DAS &amp; PWN</li>
    <li>Power Solutions</li>
  </ul>

  <h3 class="t pill-title pill-light" style="left:790px; top:221px; width:136px">OUR MARKETS</h3>
  <ul class="t list list-light" style="left:860px; top:246px">
    <li>Manufacturing &amp; Digital Supply</li>
    <li style="padding-left:6px">Chain</li>
    <li>Carriers &amp; Cable Companies</li>
    <li>Data Centers</li>
    <li>Utilities</li>
    <li>Federal Government</li>
    <li>Education</li>
  </ul>

  <h3 class="t pill-title pill-dark" style="left:625px; top:290px; width:220px">SOLUTIONS SERVICES</h3>
  <ul class="t list list-dark" style="left:682px; top:322px">
    <li>Kitting &amp; Logistics</li>
    <li>Professional Engineering</li>
    <li>Placeholder</li>
    <li>Placeholder</li>
    <li>Placeholder</li>
  </ul>
</main>
</body>
</html>
```